We require banners for Twitter, LinkedIn and Facebook.

We want 3 banners that reflect the FinTech sector. We provide outsourced sales and marketing services to Fintech companies, mature and startup. See our website at www.corvelasystems.com. We operate in Europe, Middle East , Africa and Asia Pacific. We want the banners similar, highly professional and editable.

Target Market(s)

European and Asia Pacific FinTech sector of existing or start-up companies seeking to engage as an outsourced sales and marketing services provider.

Industry/Entity Type

Marketing

Font styles to use
Sans Serif

Requirements
Must have
• A high tech financial services image
Nice to have
• Fintech infographic, banking systems, financial systems, financial or stock market images
Should not have
• cartoon or drawn images.

```html
<!DOCTYPE html>
<html lang="en">
<head>
<meta charset="utf-8">
<title>Fintech Sales &amp; Marketing Banner</title>
<link href="https://fonts.googleapis.com/css2?family=PT+Sans:wght@400;700&display=swap" rel="stylesheet">
<style>
  :root {
    --page-bg: #ffffff;
    --page-frame: #222222;
    --photo-deep: #0f2036;
    --photo-mid: #2c4560;
    --photo-light: #5d6f80;
    --overlay: rgba(18, 38, 66, 0.55);
    --text-main: #f1f3f6;
    --text-soft: #dfe4ea;
    --button-bg: #1e4c8c;
  }
  html, body {
    margin: 0;
    padding: 0;
    overflow: hidden;
  }
  body {
    width: 1200px;
    height: 1200px;
    background: var(--page-bg);
    position: relative;
    font-family: "PT Sans", "Myriad Pro", Arial, sans-serif;
  }
  .canvas-frame {
    position: absolute;
    inset: 0;
    border: 1px solid var(--page-frame);
    box-sizing: border-box;
  }
  .banner {
    position: absolute;
    left: 40px;
    top: 430px;
    width: 1120px;
    height: 340px;
    overflow: hidden;
  }
  .banner-photo {
    position: absolute;
    inset: 0;
    background:
      radial-gradient(ellipse 45% 70% at 80% 40%, var(--photo-light) 0%, transparent 70%),
      radial-gradient(ellipse 35% 50% at 15% 20%, #4a5b6c 0%, transparent 70%),
      linear-gradient(100deg, var(--photo-deep) 0%, var(--photo-mid) 35%, #3f5468 65%, var(--photo-deep) 100%);
  }
  .banner-overlay {
    position: absolute;
    inset: 0;
    background: var(--overlay);
  }
  .banner-content {
    position: absolute;
    inset: 0;
    text-align: center;
    color: var(--text-main);
  }
  .headline {
    position: absolute;
    left: 0;
    right: 0;
    top: 100px;
    margin: 0;
    font-size: 21.5px;
    line-height: 33px;
    font-weight: 400;
    letter-spacing: 0.1px;
  }
  .tagline {
    position: absolute;
    left: 0;
    right: 0;
    top: 184px;
    margin: 0;
    font-size: 16.5px;
    font-weight: 400;
    color: var(--text-soft);
  }
  .cta-button {
    position: absolute;
    left: 434px;
    top: 240px;
    width: 252px;
    height: 46px;
    line-height: 46px;
    background: var(--button-bg);
    color: var(--text-main);
    font-size: 18px;
    text-decoration: none;
  }
</style>
</head>
<body>
  <div class="canvas-frame"></div>
  <section class="banner">
    <div class="banner-photo" role="img" aria-label="Photograph of business people reviewing a printed financial report with bar charts"></div>
    <div class="banner-overlay"></div>
    <div class="banner-content">
      <h1 class="headline">EUROPEAN AND ASIA PACIFIC FINTECH SECTOR OF EXISTING OR START-UP COMPANIES<br>SEEKING TO ENGAGE AS AN OUTSOURCED SALES AND MARKETING SERVICES PROVIDER.</h1>
      <p class="tagline">CONSTANTLY CHALLENGING OURSELVES TO DELIVER MORE TO OUR CLIENTS</p>
      <a class="cta-button" href="#">GET IN TOUCH WITH US</a>
    </div>
  </section>
</body>
</html>
```